Alloy wheel repair business needs a website

Install logo previously purchased from vantoquill, toolbar with dropdowns. services, gallery, clients , contact ect
Maybe mission statment

Target Market(s)

vehicle owners, auto dealers,insurance companies,

Industry/Entity Type

Alloy Wheel Repair

Coding

Coded - Design and coding required

Number of Pages Required

4 page

Font styles to use
Sans Serif

Colors
0054AA
0677BA
7BADD7
CADEEF
E8F1F8

```html
<!DOCTYPE html>
<html lang="en">
<head>
<meta charset="utf-8">
<title>Spokecraft Wheel Co – Alloy Wheel Repair</title>
<link href="https://fonts.googleapis.com/css2?family=Roboto:wght@400;500;700;900&display=swap" rel="stylesheet">
<style>
:root{
  --brand:#0054AA;
  --brand-2:#0677BA;
  --sky:#7BADD7;
  --mist:#CADEEF;
  --ice:#E8F1F8;
  --ink:#111418;
  --muted:#555d66;
  --footer:#0c111c;
  --white:#fff;
  --star:#f6a21a;
}
*{box-sizing:border-box;margin:0;padding:0}
html,body{width:1200px;height:3958px;overflow:hidden}
body{position:relative;font-family:'Roboto',sans-serif;color:var(--ink);background:var(--white)}
.abs{position:absolute}
.btn{position:absolute;display:flex;align-items:center;justify-content:center;border-radius:30px;font-weight:500;font-size:12px;text-decoration:none}
.btn-blue{background:var(--brand);color:var(--white)}
.btn-white{background:var(--white);color:var(--brand)}
.wordmark{font-family:'Roboto',sans-serif;font-weight:900;color:var(--brand);letter-spacing:1px;display:flex;align-items:center;gap:8px}
.wordmark .dot{width:14px;height:14px;border-radius:50%;background:var(--brand)}

/* header */
.site-header{position:absolute;left:0;top:0;width:1200px;height:59px;background:var(--white)}
.site-header .wordmark{position:absolute;left:112px;top:17px;font-size:20px}
.nav{position:absolute;top:22px;font-size:12px;font-weight:500;color:var(--ink)}
.nav .caret{display:inline-block;margin-left:6px;border:4px solid transparent;border-top:5px solid var(--brand-2);vertical-align:-2px}

/* hero */
.hero{position:absolute;left:0;top:59px;width:1200px;height:586px;background:linear-gradient(90deg,#3a3c40 0%,#6a6d72 45%,#b8bcc2 75%,#8d9096 100%)}
.hero h1{position:absolute;left:112px;top:150px;font-size:46px;line-height:52px;font-weight:700;color:var(--white)}
.hero p{position:absolute;left:112px;top:282px;width:420px;font-size:10px;line-height:15px;color:var(--white)}

/* features */
.features{position:absolute;left:184px;top:545px;width:831px;height:208px;background:var(--white);border-radius:8px;box-shadow:0 6px 24px rgba(0,40,90,.12)}
.feature{position:absolute;top:30px;width:240px;text-align:center}
.feature .ring{width:72px;height:72px;margin:0 auto;border-radius:50%;border:2px solid var(--brand-2);display:flex;align-items:center;justify-content:center}
.feature h3{margin-top:20px;font-size:18px;line-height:24px;font-weight:500}

/* about */
.about-photo{position:absolute;left:112px;top:825px;width:436px;height:375px;border-radius:10px;background:linear-gradient(135deg,#cfd3d8,#5d6168 60%,#23272d)}
.about-bar{position:absolute;left:123px;top:840px;width:437px;height:372px;border-radius:10px;background:var(--brand-2)}
.about-badge{position:absolute;left:401px;top:1129px;width:183px;height:92px;background:var(--white);box-shadow:0 4px 16px rgba(0,0,0,.12);display:flex;align-items:center;justify-content:center}
.about-badge .wordmark{font-size:17px}
.about h2{position:absolute;left:620px;top:852px;font-size:37px;line-height:46px;font-weight:700}
.about h2 span{color:var(--brand-2)}
.about .copy{position:absolute;left:620px;top:966px;width:470px;font-size:11px;line-height:18.7px;color:var(--muted)}

/* services */
.services{position:absolute;left:0;top:1298px;width:1200px;height:588px;background:var(--ice)}
.sec-title{position:absolute;left:0;width:1200px;text-align:center;font-size:37px;font-weight:700}
.sec-title .hl{color:var(--brand-2)}
.pill{position:absolute;width:300px;height:54px;border-radius:27px;background:var(--white);box-shadow:0 3px 10px rgba(0,60,120,.08);display:flex;align-items:center;padding-left:46px;gap:18px;font-size:15px;font-weight:500}
.tires{position:absolute;left:442px;top:146px;width:318px;height:292px}

/* gallery */
.gallery{position:absolute;left:0;top:1886px;width:1200px;height:590px;background:var(--brand)}
.gallery .sec-title{color:var(--white)}
.compare{position:absolute;top:148px;width:298px;height:284px;border:2px solid var(--white);border-radius:4px;overflow:hidden;display:flex}
.compare .half{width:50%;height:100%}
.compare .split{position:absolute;left:148px;top:0;width:2px;height:100%;background:var(--brand)}
.compare .handle{position:absolute;left:131px;top:124px;width:36px;height:36px;border-radius:50%;background:var(--brand)}

/* testimonials */
.tcard{position:absolute;top:2627px;width:466px;height:239px;background:var(--white);box-shadow:0 4px 20px rgba(0,40,90,.1)}
.tcard .avatar{position:absolute;left:36px;top:33px;width:78px;height:78px;border-radius:50%;border:3px solid var(--brand-2);background:linear-gradient(135deg,#7a7f88,#2f343b)}
.tcard .name{position:absolute;left:140px;top:60px;font-size:15px;font-weight:500}
.tcard .stars{position:absolute;left:140px;top:80px;color:var(--star);font-size:17px;letter-spacing:1px}
.tcard .quote{position:absolute;left:68px;top:141px;width:370px;font-size:11px;line-height:18.5px;color:var(--muted)}
.tcard .qmark{position:absolute;font-size:28px;font-weight:900;color:var(--brand-2);line-height:1}
.arrow{position:absolute;width:42px;height:42px;border-radius:50%;display:flex;align-items:center;justify-content:center}
.arrow.solid{background:var(--brand-2)}
.arrow.ghost{background:var(--white);box-shadow:0 2px 10px rgba(0,0,0,.1)}

/* blog */
.post{position:absolute;top:3024px;width:317px;height:386px;background:var(--white);box-shadow:0 4px 20px rgba(0,40,90,.08)}
.post .thumb{width:100%;height:203px}
.post .meta{position:absolute;left:36px;top:228px;font-size:10px;color:var(--ink);display:flex;align-items:center;gap:8px}
.post h3{position:absolute;left:36px;top:254px;font-size:19px;font-weight:700}
.post p{position:absolute;left:36px;top:288px;width:262px;font-size:10px;line-height:18.5px;color:var(--muted)}
.post .more{position:absolute;left:36px;top:352px;font-size:12px;font-weight:500;text-decoration:underline;display:flex;align-items:center;gap:12px;color:var(--ink)}

/* cta */
.cta{position:absolute;left:0;top:3487px;width:1200px;height:230px;background:var(--brand)}
.cta h2{position:absolute;left:0;top:56px;width:1200px;text-align:center;font-size:37px;font-weight:700;color:var(--white)}

/* footer */
.site-footer{position:absolute;left:0;top:3717px;width:1200px;height:241px;background:var(--footer);color:var(--white)}
.site-footer .wordmark{position:absolute;left:112px;top:50px;font-size:22px;color:var(--white)}
.site-footer .wordmark .dot{background:var(--white)}
.fcol{position:absolute;top:48px}
.fcol h4{font-size:13px;font-weight:700;margin-bottom:12px}
.fcol li{list-style:none;font-size:11px;line-height:22px}
.social{position:absolute;top:130px;width:26px;height:26px;border-radius:50%;border:1.5px solid var(--white)}
.copyright{position:absolute;left:112px;top:181px;width:170px;font-size:9px;line-height:14px}
.newsletter{position:absolute;left:852px;top:82px;width:234px;height:36px;border:1px solid var(--white);border-radius:20px;display:flex;overflow:hidden}
.newsletter .field{flex:1;font-size:9px;display:flex;align-items:center;padding-left:22px;color:#cdd3dc}
.newsletter .go{width:86px;background:var(--brand);font-size:11px;font-weight:500;display:flex;align-items:center;justify-content:center}
</style>
</head>
<body>

<header class="site-header">
  <div class="wordmark"><span class="dot"></span>SPOKECRAFT</div>
  <nav>
    <span class="nav" style="left:449px">Home</span>
    <span class="nav" style="left:516px">About Us</span>
    <span class="nav" style="left:601px">Services<span class="caret"></span></span>
    <span class="nav" style="left:702px">Gallery</span>
    <span class="nav" style="left:776px">Clients</span>
    <span class="nav" style="left:849px">Contact</span>
  </nav>
  <a class="btn btn-blue" style="left:928px;top:12px;width:155px;height:35px">Book Appointment</a>
</header>

<section class="hero" role="img" aria-label="Mechanic in blue overalls holding wrenches beside a raised car in a workshop">
  <h1>Experts in Alloy Wheel<br>Auto Repair</h1>
  <p>Lorem ipsum dolor sit amet, consectetur adipiscing elit, sed do eiusmod tempor incididunt ut labore et dolore magna aliqua. Quis ipsum suspendisse ultrices gravida. Risus commodo viverra maecenas accumsan lacus vel facilisis.</p>
  <a class="btn btn-blue" style="left:112px;top:356px;width:131px;height:36px">Contact Us</a>
</section>

<section class="features">
  <div class="feature" style="left:32px">
    <div class="ring"><svg width="34" height="34" viewBox="0 0 34 34" fill="none" stroke="#0677BA" stroke-width="2"><circle cx="17" cy="15" r="8"/><circle cx="17" cy="15" r="3"/><path d="M4 22c4 0 6 6 13 6s9-6 13-6"/></svg></div>
    <h3>Highly Trained<br>Mechanics</h3>
  </div>
  <div class="feature" style="left:269px">
    <div class="ring"><svg width="30" height="32" viewBox="0 0 30 32"><path d="M15 2l11 4v9c0 8-5 13-11 15C9 28 4 23 4 15V6z" fill="#0054AA"/><path d="M10 16l4 4 7-8" stroke="#fff" stroke-width="2.5" fill="none"/></svg></div>
    <h3>Transparent<br>Prices</h3>
  </div>
  <div class="feature" style="left:522px">
    <div class="ring"><svg width="30" height="30" viewBox="0 0 30 30" fill="#0677BA"><rect x="3" y="13" width="6" height="14" rx="1"/><path d="M11 13l5-9c2 0 3 1 3 3l-1 5h7c2 0 3 2 2 4l-3 9c-1 2-2 2-4 2H11z"/></svg></div>
    <h3>Golden Rule/Good Work<br>Open Book Guarantees</h3>
  </div>
</section>

<section class="about">
  <div class="about-bar"></div>
  <div class="about-photo" role="img" aria-label="Technician tightening lug nuts on an alloy wheel of a white car"></div>
  <div class="about-badge"><div class="wordmark"><span class="dot"></span>SPOKECRAFT</div></div>
  <h2><span>Alloy Wheel Work</span><br>About Us</h2>
  <div class="copy">
    <p>Your vehicle is most likely the second largest investment that you will make, next to your home. Don't entrust its value and restoration to the cheapest offer, or some big name shop that sees you only as another number.</p>
    <p>At Ridgeline Rim Solutions We are determined to make your repair experience as painless as possible. We understand that accidents are never planned and can cause a lot of anxiety and stress. We see PEOPLE needing service, NOT a ticket to make money. We strive to ensure each customer receives not only the best repair possible, but the highest standard of customer service as well.</p>
  </div>
  <a class="btn btn-blue" style="left:620px;top:1152px;width:132px;height:36px">Read More</a>
</section>

<section class="services">
  <h2 class="sec-title" style="top:56px">Our <span class="hl">Services</span></h2>
  <div class="pill" style="left:112px;top:177px"><svg width="30" height="30" viewBox="0 0 30 30" fill="none" stroke="#0677BA" stroke-width="2"><circle cx="15" cy="15" r="12"/><circle cx="15" cy="15" r="3"/><path d="M15 3v9M15 18v9M3 15h9M18 15h9"/></svg>Wheel Refinishing</div>
  <div class="pill" style="left:112px;top:253px"><svg width="30" height="30" viewBox="0 0 30 30"><circle cx="15" cy="15" r="11" fill="none" stroke="#0677BA" stroke-width="6" stroke-dasharray="4 3"/><circle cx="15" cy="15" r="5" fill="#0677BA"/></svg>Wheel Remanufacturing</div>
  <div class="pill" style="left:112px;top:329px"><svg width="30" height="30" viewBox="0 0 30 30" fill="none" stroke="#0677BA" stroke-width="2"><circle cx="15" cy="15" r="12"/><path d="M15 7l2.5 5 5.5.8-4 3.9 1 5.5-5-2.6-5 2.6 1-5.5-4-3.9 5.5-.8z"/></svg>Curb Damage Repair</div>
  <div class="pill" style="left:112px;top:405px"><svg width="30" height="30" viewBox="0 0 30 30" fill="none" stroke="#0677BA" stroke-width="2"><circle cx="18" cy="15" r="10"/><circle cx="18" cy="15" r="3"/><path d="M3 7h5M2 12h5M2 18h5M3 23h5"/></svg>Wheel Straightening</div>

  <div class="pill" style="left:783px;top:177px"><svg width="30" height="30" viewBox="0 0 30 30" fill="none" stroke="#0677BA" stroke-width="2"><circle cx="15" cy="15" r="12"/><circle cx="15" cy="15" r="3"/><path d="M15 3l-2 9M25 11l-8 4M9 25l5-7"/></svg>Cracked Wheel Repair</div>
  <div class="pill" style="left:783px;top:253px"><svg width="30" height="30" viewBox="0 0 30 30" fill="none" stroke="#0677BA" stroke-width="2"><circle cx="15" cy="15" r="12"/><circle cx="15" cy="15" r="3"/><path d="M15 3v9M4 12l8 2M8 25l5-8M22 25l-5-8M26 12l-8 2"/></svg>Rim Straightening</div>
  <div class="pill" style="left:783px;top:329px"><svg width="30" height="30" viewBox="0 0 30 30" fill="none" stroke="#0677BA" stroke-width="2"><path d="M5 20a10 10 0 0 1 20 0"/><path d="M9 20a6 6 0 0 1 12 0"/><path d="M3 23h24M3 27h24"/></svg>Wheel and Tire Sales</div>
  <div class="pill" style="left:783px;top:405px"><svg width="30" height="30" viewBox="0 0 30 30" fill="none" stroke="#0677BA" stroke-width="2"><circle cx="19" cy="15" r="9"/><circle cx="19" cy="15" r="3"/><path d="M2 10h7M2 15h6M2 20h7"/></svg>Powder Coating</div>

  <svg class="tires" viewBox="0 0 318 292" aria-hidden="true">
    <circle cx="190" cy="70" r="68" fill="none" stroke="#CADEEF" stroke-width="1.5"/>
    <circle cx="190" cy="70" r="50" fill="none" stroke="#CADEEF" stroke-width="1.5"/>
  </svg>
  <div role="img" aria-label="Stack of black tyres beside an alloy wheel" style="position:absolute;left:442px;top:220px;width:318px;height:216px;border-radius:40px;background:radial-gradient(circle at 68% 50%,#9aa0a8 0 18%,#2a2c30 40%,#121315 70%)"></div>
  <a class="btn btn-blue" style="left:516px;top:495px;width:168px;height:36px">View All Services</a>
</section>

<section class="gallery">
  <h2 class="sec-title" style="top:54px">Our Gallery</h2>
  <div class="compare" style="left:112px" role="img" aria-label="Before and after: rusted wheel restored to a bright silver alloy">
    <div class="half" style="background:linear-gradient(135deg,#b59a76,#5a4a3c)"></div>
    <div class="half" style="background:linear-gradient(135deg,#e8eaed,#7d8289)"></div>
    <div class="split"></div><div class="handle"></div>
  </div>
  <div class="compare" style="left:450px" role="img" aria-label="Before and after: damaged rim on a flat tyre repaired and refitted">
    <div class="half" style="background:linear-gradient(135deg,#c9c2b6,#6e6a62)"></div>
    <div class="half" style="background:linear-gradient(135deg,#6c7178,#25282c)"></div>
    <div class="split"></div><div class="handle"></div>
  </div>
  <div class="compare" style="left:788px" role="img" aria-label="Before and after: scuffed wheel refinished to a clean silver face">
    <div class="half" style="background:linear-gradient(135deg,#2e3136,#a3a7ad)"></div>
    <div class="half" style="background:linear-gradient(135deg,#3a3d42,#dfe2e6)"></div>
    <div class="split"></div><div class="handle"></div>
  </div>
  <svg style="position:absolute;left:0;top:0" width="1200" height="590" aria-hidden="true">
    <g fill="#fff"><path d="M257 2177l-6 5 6 5zM265 2177l6 5-6 5z" transform="translate(0,-1886)"/>
    <path d="M595 2177l-6 5 6 5zM603 2177l6 5-6 5z" transform="translate(0,-1886)"/>
    <path d="M933 2177l-6 5 6 5zM941 2177l6 5-6 5z" transform="translate(0,-1886)"/></g>
  </svg>
  <a class="btn btn-white" style="left:516px;top:493px;width:168px;height:37px">View All Repairs</a>
</section>

<section class="testimonials">
  <h2 class="sec-title" style="top:2530px"><span class="hl">What Our</span> Clients Say</h2>
  <div class="arrow ghost" style="left:43px;top:2724px"><svg width="18" height="14" viewBox="0 0 18 14" fill="none" stroke="#0677BA" stroke-width="1.6"><path d="M17 7H2M7 1L1 7l6 6"/></svg></div>
  <div class="arrow solid" style="left:1113px;top:2724px"><svg width="18" height="14" viewBox="0 0 18 14" fill="none" stroke="#fff" stroke-width="1.6"><path d="M1 7h15M11 1l6 6-6 6"/></svg></div>
  <article class="tcard" style="left:112px">
    <div class="avatar" role="img" aria-label="Customer portrait"></div>
    <div class="name">Dorian Vale</div>
    <div class="stars">★★★★★</div>
    <span class="qmark" style="left:36px;top:135px">&ldquo;</span>
    <p class="quote">Lorem ipsum dolor sit amet, consectetur adipiscing elit. Pellentesque fermentum iaculis mi nec volutpat. Cras sollicitudin, nibh non malesuada auctor, turpis augue tempus arcu, eget ultricies lorem leo at felis.Proin molestie massa in nisl gravida, ac cursus elit efficitur.</p>
    <span class="qmark" style="left:352px;top:198px">&rdquo;</span>
  </article>
  <article class="tcard" style="left:620px">
    <div class="avatar" role="img" aria-label="Customer portrait"></div>
    <div class="name">Nina Castell</div>
    <div class="stars">★★★★★</div>
    <span class="qmark" style="left:36px;top:135px">&ldquo;</span>
    <p class="quote">Lorem ipsum dolor sit amet, consectetur adipiscing elit. Pellentesque fermentum iaculis mi nec volutpat. Cras sollicitudin, nibh non malesuada auctor, turpis augue tempus arcu, eget ultricies lorem leo at felis.Proin molestie massa in nisl gravida, ac cursus elit efficitur.</p>
    <span class="qmark" style="left:352px;top:198px">&rdquo;</span>
  </article>
</section>

<section class="blog">
  <h2 class="sec-title" style="top:2930px">Our Latest <span class="hl">Blog</span></h2>
  <div class="arrow solid" style="left:43px;top:3198px"><svg width="18" height="14" viewBox="0 0 18 14" fill="none" stroke="#fff" stroke-width="1.6"><path d="M17 7H2M7 1L1 7l6 6"/></svg></div>
  <div class="arrow ghost" style="left:1113px;top:3198px"><svg width="18" height="14" viewBox="0 0 18 14" fill="none" stroke="#0677BA" stroke-width="1.6"><path d="M1 7h15M11 1l6 6-6 6"/></svg></div>

  <article class="post" style="left:112px">
    <div class="thumb" role="img" aria-label="Roadside tyre change beside a car with its hood open" style="background:linear-gradient(135deg,#c9ccd0,#5b5f66 55%,#2b2e33)"></div>
    <div class="meta"><svg width="12" height="12" viewBox="0 0 12 12" fill="none" stroke="#111" stroke-width="1.2"><circle cx="6" cy="6" r="5"/><path d="M6 3v3l2 1"/></svg>July 20, 2023 &nbsp;|&nbsp; <svg width="12" height="10" viewBox="0 0 12 10" fill="none" stroke="#111" stroke-width="1.1"><path d="M1 1h4l1 1.5h5V9H1z"/></svg>Blogs</div>
    <h3>How to Change a Tire</h3>
    <p>Changing a tire is an important life skill that any driver needs to know. However, not every driver learns this skill before hitting the road.</p>
    <a class="more">Read More <svg width="16" height="10" viewBox="0 0 16 10" fill="none" stroke="#0677BA" stroke-width="1.4"><path d="M0 5h14M10 1l4 4-4 4"/></svg></a>
  </article>
  <article class="post" style="left:442px">
    <div class="thumb" role="img" aria-label="Mechanic fitting a tyre in a workshop" style="background:linear-gradient(135deg,#9aa3ad,#3d434b 55%,#1c1f24)"></div>
    <div class="meta"><svg width="12" height="12" viewBox="0 0 12 12" fill="none" stroke="#111" stroke-width="1.2"><circle cx="6" cy="6" r="5"/><path d="M6 3v3l2 1"/></svg>May 20, 2023 &nbsp;|&nbsp; <svg width="12" height="10" viewBox="0 0 12 10" fill="none" stroke="#111" stroke-width="1.1"><path d="M1 1h4l1 1.5h5V9H1z"/></svg>Blogs</div>
    <h3>Wheel Alignment</h3>
    <p>World class for 125 years! Over the past 125 years Harlan has built up a reputation of excellence within the automotive industry.</p>
    <a class="more">Read More <svg width="16" height="10" viewBox="0 0 16 10" fill="none" stroke="#0677BA" stroke-width="1.4"><path d="M0 5h14M10 1l4 4-4 4"/></svg></a>
  </article>
  <article class="post" style="left:771px">
    <div class="thumb" role="img" aria-label="Technician showing a customer a wheel in a service bay" style="background:linear-gradient(135deg,#2a5a9a,#6f7c8c 50%,#b43a3a)"></div>
    <div class="meta"><svg width="12" height="12" viewBox="0 0 12 12" fill="none" stroke="#111" stroke-width="1.2"><circle cx="6" cy="6" r="5"/><path d="M6 3v3l2 1"/></svg>June 15, 2023 &nbsp;|&nbsp; <svg width="12" height="10" viewBox="0 0 12 10" fill="none" stroke="#111" stroke-width="1.1"><path d="M1 1h4l1 1.5h5V9H1z"/></svg>Blogs</div>
    <h3>Tire Pressure</h3>
    <p>Tires are literally where the rubber hits the road, and they play a huge part in how your vehicle performs overall.</p>
    <a class="more">Read More <svg width="16" height="10" viewBox="0 0 16 10" fill="none" stroke="#0677BA" stroke-width="1.4"><path d="M0 5h14M10 1l4 4-4 4"/></svg></a>
  </article>
</section>

<section class="cta">
  <h2>Contact Us &amp; Get An Estimate Today</h2>
  <a class="btn btn-white" style="left:516px;top:133px;width:168px;height:37px">Schedule Services</a>
</section>

<footer class="site-footer">
  <div class="wordmark"><span class="dot"></span>SPOKECRAFT</div>
  <span class="social" style="left:112px"></span>
  <span class="social" style="left:153px"></span>
  <span class="social" style="left:194px"></span>
  <p class="copyright">Copyright © 2023 Spokecraft Wheel Co - All rights reserved.</p>
  <div class="fcol" style="left:324px"><h4>QUICK LINK</h4><ul><li>Home</li><li>About Us</li><li>Services</li><li>Contact Us</li><li>Testimonials</li><li>Blog</li></ul></div>
  <div class="fcol" style="left:468px"><h4>OUR SERVICES</h4><ul><li>Wheel Refinishing</li><li>Wheel Remanufacturing</li><li>Curb Rash Repair</li><li>Wheel Straightening</li><li>Cracked Wheel Repair</li><li>Rim Straightening</li></ul></div>
  <div class="fcol" style="left:647px"><h4>CONTACT US</h4><ul><li>555 - 014 - 2290</li><li>742 Orchard Mill Road</li><li>Brookfield PA</li><li>hello@spokecraftwheel.com</li></ul></div>
  <div class="fcol" style="left:852px"><h4>SUBSCRIBE TO OUR NEWSLETTER</h4></div>
  <div class="newsletter"><span class="field">Enter your email</span><span class="go">Subscribe</span></div>
</footer>

</body>
</html>
```